Flyer-Design für Gefäßchirurg
Zielgruppe
Niedergelassener Gefäßchirurg in eigener (Einzel-) Praxis; zZt 4 Angestellte (1 Krankenschwester, eine MFA, eine Azubi, eine Reinigungskraft); tätig in der Stadt Plön (24306); im Kreis Plön nur ein weiter ALLGEMEIN chirurg; HP: www.praxisdoktor-haverbeck.de ; Kernkompetenz: Diagnostik und Therapie von Gefäßerkrankungen (z.B. Krampfadern, Durchblutungsstörungen... (s.auch HP); eigener OP in der Praxis; hier Versorgung u.a. von Krampfadern aber auch andere chirurgische Eingriffe;
Aufgabenstellung
Bzgl. des Formates keine Festlegung bevorzuge aber Format Din lang hoch oder Din a 5 hoch ; Flyer soll übersichtlich Behandlungen der Praxis benennen; insbesondere um auch außerhalb der Gefäßchirurgie weitere chirurgische Patienten zu gewinnen (z.B. chirurgische Entfernung kleiner Pigmentflecke, eingewachsener Nagel, aber auch 'Wegspritzen/ Sklerosierung' von Besenreisern, eingewachsener Zehennagel), ggf. mit Anfahrtskarte, Parkplätze vor der Tür; falls nicht zu Kostenintensiv: auch Nutzung von Stock - Bildern (ca. Obergrenze für Bildmaterial 50,- €);
mir ist bewusst, dass die Photos der Angestellten und mir nicht 100% scharf sind; falls diese verwendet werden, könnten diese z.B. kleinformatig auf dem flyer erscheinen, oder ich würde diese im Verlauf noch einmal aufnehmen. Ob und wieviele der Photos auf dem flyer sind, überlasse ich Ihnen.

```html
<!DOCTYPE html>
<html lang="de">
<head>
<meta charset="utf-8">
<title>Flyer Praxis für Gefäßmedizin und Chirurgie</title>
<link href="https://fonts.googleapis.com/css2?family=Montserrat:wght@400;500;600;700;800&display=swap" rel="stylesheet">
<style>
:root{
  --red:#c8232c;
  --dark:#444446;
  --light:#f1f1f1;
  --white:#ffffff;
  --text:#4a4a4a;
  --muted:#8a8a8a;
  --bg:#e6e6e6;
}
*{margin:0;padding:0;box-sizing:border-box}
html,body{width:1200px;height:2400px;overflow:hidden}
body{background:var(--bg);font-family:'Montserrat',sans-serif;color:var(--text);position:relative}
.spread{position:absolute;left:50px;width:1100px;height:780px;display:flex;box-shadow:0 12px 30px rgba(0,0,0,.18);border-top:6px solid var(--red);border-bottom:6px solid var(--red)}
.spread--outside{top:270px}
.spread--inside{top:1340px;background:var(--white)}
.panel{position:relative;width:550px;height:100%;overflow:hidden}
.panel--back{background:var(--dark);color:var(--white)}
.panel--cover{background:var(--light)}
.brand{position:absolute;right:40px;top:40px;text-align:right}
.brand__name{font-size:30px;font-weight:600;letter-spacing:.5px;display:flex;align-items:center;justify-content:flex-end;gap:10px}
.brand__dot{width:14px;height:14px;border-radius:50%;background:var(--red)}
.brand__sub{font-size:12px;font-weight:500;margin-top:2px}
.panel--back .brand__sub{color:#d0d0d0}
.panel--cover .brand__name{color:#3c3c3c}
.map{position:absolute;left:95px;top:120px;width:240px;height:240px;border-radius:50%;background:linear-gradient(135deg,#f4f4f4 55%,#bcd8ea)}
.badge{position:absolute;border-radius:50%;background:var(--red);color:var(--white);display:flex;flex-direction:column;align-items:center;justify-content:center;text-align:center;line-height:1}
.badge--map{left:275px;top:285px;width:110px;height:110px;border:4px solid var(--dark);font-weight:800;font-size:13px;transform:rotate(-12deg)}
.badge--map small{font-size:10px;font-weight:500;margin-top:3px}
.contact{position:absolute;left:80px;top:415px;list-style:none}
.contact li{display:flex;align-items:center;gap:14px;font-size:14px;font-weight:500;height:30px}
.contact svg{width:20px;height:20px}
.hours{position:absolute;left:80px;top:560px;font-size:13px;line-height:1.55}
.hours h3{font-size:12px;font-weight:700;margin-bottom:10px}
.hours p{margin-bottom:8px}
.back-rule{position:absolute;left:80px;right:70px;top:700px;height:1px;background:var(--red)}
.web{position:absolute;left:80px;top:720px;font-size:17px;font-weight:500}
.photo{position:absolute;left:20px;top:125px;width:390px;height:390px;border-radius:50%;background:radial-gradient(circle at 45% 40%,#e8e8ea,#c9ccd3 60%,#b9a0a6)}
.badge--cta{left:50px;top:425px;width:130px;height:130px;font-weight:800;font-size:23px}
.badge--cta small{font-size:16px;font-weight:500;margin-top:4px}
.cover-title{position:absolute;left:50px;top:590px;color:var(--red);font-weight:700}
.cover-title__main{font-size:42px;display:flex;align-items:flex-end;gap:6px}
.cover-title__main::after{content:"";display:block;width:200px;height:2px;background:var(--red);margin-bottom:10px}
.cover-title__sub{font-size:42px;display:flex;align-items:baseline;gap:8px}
.cover-title__sub span{font-size:20px;border-top:2px solid var(--red);padding-top:2px}
.heading{color:var(--red);font-weight:700;font-size:32px;line-height:1}
.heading small{display:block;color:var(--text);font-size:15px;font-weight:600}
.heading::after{content:"";display:block;width:140px;height:1px;background:var(--red);margin-top:6px}
.praxis-head{position:absolute;left:45px;top:40px}
.portrait{position:absolute;left:250px;top:20px;width:170px;height:170px;border-radius:50%;background:linear-gradient(160deg,#d9c6b0,#8a7d70)}
.body{font-size:12.5px;line-height:1.45}
.praxis-text{position:absolute;left:45px;top:130px;width:420px}
.praxis-text p{margin-bottom:8px}
.praxis-text p:first-child{width:190px}
.team-head{position:absolute;left:45px;top:445px}
.team-text{position:absolute;left:45px;top:530px;width:380px}
.team{position:absolute;left:45px;top:600px;display:flex;gap:30px}
.member{width:120px;text-align:center}
.member__photo{width:110px;height:110px;border-radius:50%;margin:0 auto 8px;background:linear-gradient(160deg,#e0c9b4,#7e6a5c)}
.member__name{font-size:12px}
.member__role{display:inline-block;background:var(--red);color:var(--white);font-size:11px;padding:1px 6px;margin-top:2px}
.panel--services{border-left:1px solid #eee}
.services-head{position:absolute;left:40px;top:40px}
.badge--small{right:35px;top:40px;width:80px;height:80px;background:var(--dark);font-size:13px;font-weight:800}
.badge--small small{font-size:10px;font-weight:500;margin-top:2px}
.services{position:absolute;left:40px;top:115px;width:470px;list-style:none}
.services li{margin-bottom:9px}
.services h4{font-size:12.5px;font-weight:700;text-transform:uppercase;color:#3c3c3c}
.services p{font-size:10.5px;display:flex;gap:6px;align-items:flex-start;line-height:1.3}
.services p svg{flex:none;width:11px;height:11px;margin-top:1px}
.cta-box{position:absolute;left:0;right:0;bottom:0;height:195px;background:var(--red);color:var(--white)}
.cta-box__text{position:absolute;left:40px;right:30px;top:20px;text-align:center;font-size:15px;font-weight:600;line-height:1.35}
.cta-box__phone{position:absolute;left:40px;top:105px;width:56px;height:56px}
.cta-box__frame{position:absolute;left:120px;right:30px;top:95px;height:80px;border:2px solid var(--white);text-align:center;padding-top:6px;font-size:14px;font-weight:500;line-height:1.2}
.cta-box__frame strong{display:block;font-size:28px;font-weight:800}
</style>
</head>
<body>

<section class="spread spread--outside">
  <div class="panel panel--back">
    <div class="brand">
      <div class="brand__name"><span class="brand__dot"></span>Dr. Jan Haverbeck</div>
      <div class="brand__sub">Praxis für Gefäßmedizin und Chirurgie</div>
    </div>
    <div class="map" role="img" aria-label="Anfahrtskarte zur Praxis"></div>
    <div class="badge badge--map">LINDENALLEE<small>IN SEEBRÜCK</small></div>
    <ul class="contact">
      <li><svg viewBox="0 0 20 20"><circle cx="10" cy="10" r="10" fill="#c8232c"/><path d="M10 4a4 4 0 0 0-4 4c0 3 4 8 4 8s4-5 4-8a4 4 0 0 0-4-4z" fill="#fff"/><circle cx="10" cy="8" r="1.5" fill="#c8232c"/></svg>Lindenallee 12 | 24999 Seebrück</li>
      <li><svg viewBox="0 0 20 20"><circle cx="10" cy="10" r="10" fill="#c8232c"/><path d="M5 8c0-2 10-2 10 0v1h-3V8H8v1H5z M6 10h8l1 5H5z" fill="#fff"/></svg>Telefon: 04599 5518 300</li>
      <li><svg viewBox="0 0 20 20"><circle cx="10" cy="10" r="10" fill="#c8232c"/><rect x="7" y="5" width="6" height="4" fill="#fff"/><rect x="5" y="9" width="10" height="6" fill="#fff"/></svg>Fax: 04599 5518 309</li>
      <li><svg viewBox="0 0 20 20"><circle cx="10" cy="10" r="10" fill="#c8232c"/><rect x="5" y="6" width="10" height="8" fill="#fff"/><path d="M5 6l5 4 5-4" stroke="#c8232c" fill="none"/></svg>info@praxisdoktor-haverbeck.de</li>
    </ul>
    <div class="hours">
      <h3>ÖFFNUNGSZEITEN:</h3>
      <p>Montag, Mittwoch, Donnerstag, Freitag:<br>08:00 – 13:00 Uhr</p>
      <p>Dienstag:<br>08:00 – 13:00 13:00 – 15:00 Uhr</p>
    </div>
    <div class="back-rule"></div>
    <div class="web">www.praxisdoktor-haverbeck.de</div>
  </div>
  <div class="panel panel--cover">
    <div class="brand">
      <div class="brand__name"><span class="brand__dot"></span>Dr. Jan Haverbeck</div>
      <div class="brand__sub">Praxis für Gefäßmedizin und Chirurgie</div>
    </div>
    <div class="photo" role="img" aria-label="Stethoskop auf einem Schreibtisch, Arzt unscharf im Hintergrund"></div>
    <div class="badge badge--cta">JETZT<br>TERMIN<small>vereinbaren</small></div>
    <div class="cover-title">
      <div class="cover-title__main">Chirurgie</div>
      <div class="cover-title__sub"><span>und</span>Gefäßmedizin</div>
    </div>
  </div>
</section>

<section class="spread spread--inside">
  <div class="panel panel--praxis">
    <h2 class="heading praxis-head"><small>Die</small>Praxis</h2>
    <div class="portrait" role="img" aria-label="Porträtfoto des Arztes"></div>
    <div class="body praxis-text">
      <p>Gerne kümmern wir uns um Ihre chirurgischen und gefäß-medizinischen Anliegen.</p>
      <p>Als Gefäßchirurg und Phlebologe besitze ich eine besondere Erfahrung in der Therapie und Diagnostik von gefäßmedizinischen Erkrankungen. Mit einem hochwertigen Ultraschallgerät sowie durch einen in die Praxis integrierten Operationsraum und einem Aufwachraum sind optimale Bedingungen gegeben.</p>
      <p>Bezüglich der operativen Versorgung des Krampfaderleidens halten wir alle gängigen Operationsmethoden vor.</p>
      <p>Abseits der gefäßmedizinischen Erkrankungen sind wir auch für kleinere chirurgische Maßnahmen Ihr Ansprechpartner.</p>
    </div>
    <h2 class="heading team-head"><small>Das</small>Praxisteam</h2>
    <p class="body team-text">Unterstützt wird mein Team durch eine Krankenschwester, eine Medizinische Fachangestellte und eine Auszubildende.</p>
    <div class="team">
      <div class="member"><div class="member__photo" role="img" aria-label="Foto einer Mitarbeiterin"></div><div class="member__name">Lena Kroll</div><span class="member__role">Krankenschwester</span></div>
      <div class="member"><div class="member__photo" role="img" aria-label="Foto einer Mitarbeiterin"></div><div class="member__name">Anke Petersen</div><span class="member__role">Krankenschwester</span></div>
      <div class="member"><div class="member__photo" role="img" aria-label="Foto einer Mitarbeiterin"></div><div class="member__name">Svenja Marten</div><span class="member__role">Krankenschwester</span></div>
    </div>
  </div>
  <div class="panel panel--services">
    <h2 class="heading services-head"><small>Unsere</small>Leistungen</h2>
    <div class="badge badge--small">JETZT<br>TERMIN<small>vereinbaren</small></div>
    <ul class="services">
      <li><h4>Krampfadern</h4><p><svg viewBox="0 0 12 12"><circle cx="6" cy="6" r="6" fill="#c8232c"/><path d="M3 6l2 2 4-4" stroke="#fff" fill="none" stroke-width="1.5"/></svg>Behandeln wir konservativ, operativ oder schonend durch eine Laserbehandlung</p></li>
      <li><h4>Besenreiser</h4><p><svg viewBox="0 0 12 12"><circle cx="6" cy="6" r="6" fill="#c8232c"/><path d="M3 6l2 2 4-4" stroke="#fff" fill="none" stroke-width="1.5"/></svg>Verödung durch gezielte Sklerosierung, schonend und ambulant in unserer Praxis.</p></li>
      <li><h4>Schaufensterkrankheit</h4><p><svg viewBox="0 0 12 12"><circle cx="6" cy="6" r="6" fill="#c8232c"/><path d="M3 6l2 2 4-4" stroke="#fff" fill="none" stroke-width="1.5"/></svg>Behandeln wir konservativ, operativ oder schonend durch eine Laserbehandlung</p></li>
      <li><h4>Pigmentflecken/kleine Hauttumore</h4><p><svg viewBox="0 0 12 12"><circle cx="6" cy="6" r="6" fill="#c8232c"/><path d="M3 6l2 2 4-4" stroke="#fff" fill="none" stroke-width="1.5"/></svg>Wir bieten chirurgische Entfernungen an &amp; schicken die Befunde für weitere Untersuchungen weiter.</p></li>
      <li><h4>Bauchaortenaneurysma</h4><p><svg viewBox="0 0 12 12"><circle cx="6" cy="6" r="6" fill="#c8232c"/><path d="M3 6l2 2 4-4" stroke="#fff" fill="none" stroke-width="1.5"/></svg>Behandeln wir konservativ, operativ oder schonend durch eine Laserbehandlung</p></li>
      <li><h4>Bewertung des Schlaganfallrisikos</h4><p><svg viewBox="0 0 12 12"><circle cx="6" cy="6" r="6" fill="#c8232c"/><path d="M3 6l2 2 4-4" stroke="#fff" fill="none" stroke-width="1.5"/></svg>Behandeln wir konservativ, operativ oder schonend durch eine Laserbehandlung</p></li>
      <li><h4>Durchblutungsstörung Hände/Füße</h4><p><svg viewBox="0 0 12 12"><circle cx="6" cy="6" r="6" fill="#c8232c"/><path d="M3 6l2 2 4-4" stroke="#fff" fill="none" stroke-width="1.5"/></svg>Behandeln wir konservativ, operativ oder schonend durch eine Laserbehandlung</p></li>
      <li><h4>Nagelbettentzündung</h4><p><svg viewBox="0 0 12 12"><circle cx="6" cy="6" r="6" fill="#c8232c"/><path d="M3 6l2 2 4-4" stroke="#fff" fill="none" stroke-width="1.5"/></svg>Behandeln wir konservativ oder chirurgisch. Nur bei sehr kleinen Befunden ohne Anhaltspunkte für Abszedierung und ohne Allgemeinsymptome ist eine konservative Therapie erfolgsversprechend.</p></li>
      <li><h4>Steißbeinfistel</h4><p><svg viewBox="0 0 12 12"><circle cx="6" cy="6" r="6" fill="#c8232c"/><path d="M3 6l2 2 4-4" stroke="#fff" fill="none" stroke-width="1.5"/></svg>Nach entsprechender Diagnostik können unter ambulanten Bedingungen diese Fistelgänge chirurgisch entfernt werden.</p></li>
    </ul>
    <div class="cta-box">
      <p class="cta-box__text">Wir bieten unseren Patienten eine Terminsprechstunde an. Dies hat den Vorteil, dass Wartezeiten auf ein Minimum beschränkt werden.</p>
      <svg class="cta-box__phone" viewBox="0 0 56 56"><circle cx="28" cy="28" r="26" fill="none" stroke="#fff" stroke-width="2"/><path d="M18 16l6 0 2 7-4 3c2 4 5 7 9 9l3-4 7 2v6c0 2-2 3-4 3-12-1-20-9-21-21 0-2 1-5 2-5z" fill="#fff"/></svg>
      <div class="cta-box__frame">Gerne vergeben wir Ihnen unter<strong>04599 5518300</strong>einen für Sie passenden Termin.</div>
    </div>
  </div>
</section>

</body>
</html>
```